Kelvanta (www.kelvanta.net) needs exciting professional PowerPoint pitch template

Kelvanta is an exciting new start-up targeting innovative ways to engage with retail customers at the point of sale.

Our customers are looking for us to help them increase the "wallet share" of their retail customers. The retail customer has their wallet open at the Point of Sale and are paying money to our customer. At Kelvanta we are all about attracting the attention of the retail customer AT THAT POINT IN TIME and engaging the retail customer in spending a little more in that store or another store that has a relationship to the retail customer's purchase.

Our customers are the owners of very large supermarkets, chain stores, and financial institutions, and therefore when we pitch a proposal to these buyers it needs to be slick, professional, and very memorable.

The PowerPoint sales presentation template is a key part of striking that impression.

Here is some background...

Our Vision
Through applying new thinking to a mature industry we are reinventing selected segments of the Australian retail messaging business, generating significant value for our customers, our suppliers, and our owners.
We operate with integrity, agility, and intelligence to doing things smarter, faster and more efficiently.
We bring deep industry expertise, deep relationships with customers and suppliers, and a will to see the old ways give way to smarter ways – this is why we win.
From this economically sustainable platform, we will examine the disruption of other market segments by further leveraging the elements that make us successful.

Our Values
With our clients, with our suppliers, with our staff, and with our owners:
# We Partner – We align the interest of all stakeholders by striving to ensure everything we do is mutually beneficial and commercially sustainable in the long term. We are clear with all our stakeholders about what our expectations are of them, and we seek clarity from them in their expectations of us.
# We Innovate – In the segments we choose to compete in, we bring fresh ideas, new business processes, the right relationships, and the right technology to ensure the supply chain is nimble, competitive, and reliable.
# We are Accountable – We say what we will do, and then do what we say.
# We Perform – We use our skills, relationships, and reputation to deliver value to our customers, suppliers, and owners.

Initially we are building our business from low-tech through printing promotional offers and retailer messages on ATM and EFTPOS receipts, but as soon as cash flow supports it we will be engaging in high-tech real-time targeted offers to the specific consumer through video wall offers as people are at the checkout or walking through the shopping centre.

I'd like the PowerPoint template to reflect our vision and values.

The PowerPoint template will be used in communicating our proposals to our clients, and needs to catch and hold our audiences attention.

Please check out the web site we have just launched - it is pretty basic but it has only been up a week. We intend to sharpen it over the coming weeks, but you'll get the idea of what our core messages are.

I have recently sourced a logo from ArtHarbor, plus business cards, and have attached the source files for your reference.
Updates

Hi everybody.  Thanks for the designs submitted so far.  Your submissions have helped me understand what I do and don't prefer, and I have updated the "Must Have/Nice to Have/Shouldn't Have" criteria accordingly.  I have also uploaded a powerpoint template that I had at a company I udsed to run that has the sort of visual theme I find appealing. I have more time to provide feedback now that the week is over, so I will comment on individual designs shortly, and I will respond to queries directed to me.

Kind Regards - Grant

Target Market(s)

Our customers are large corporations that have professional Point Of Sale marketing experts looking for a supplier with an edge over others in a crowded market. The buyer of our product and services is ultimately a communications expert. They want to see distinctive competence, and an agility of thinking that will make them money through driving more consumer spending.

Industry/Entity Type

Financial

Font styles to use
Sans Serif

Colors
34a7d7
0892cd
3276b5

Requirements
Must have
• The following Slides: Title Slide, Agenda, About Kelvanta, Thank you
The pages must be easy on the eye.
The final product must be a PowerPoint template file with the usual "Title", "Title and Content", "Title & Table", and "Blank" page types.
Widescreen format please.
Nice to have
• The pages should have an eye-catching visual element running through all the pages. I have attached a template from a company i used to be involved with that has a visual theme running through it that I like.
Plenty of whitespace - have a look at www.kelvanta.net.
Bonus points for pulling the text from the brief into the template.
Use "Innovation - Integrity - Service" as the tag line.
Should not have
• Pages should not be busy.
Stay away from too much black. I know the cards have black, but the presentation shouldn't.
I dont like serifed fonts. Use Dravelle's Modern UI style for insporation.
The "Bringing Lumora" tag line was an invention of the logo designer that we do not want to cary forward. Please do not use it.

```html
<!DOCTYPE html>
<html lang="en">
<head>
<meta charset="utf-8">
<title>Kelvanta Presentation Template</title>
<link href="https://fonts.googleapis.com/css2?family=Graduate&family=Open+Sans:wght@400;600;700&display=swap" rel="stylesheet">
<style>
  :root {
    --blue: #29a8e0;
    --blue-deep: #0a78c0;
    --blue-band: #0b2233;
    --ink: #0c0c0c;
    --slide-mid: #2a2a2a;
    --white: #ffffff;
    --grey: #8a8a8a;
    --grey-dark: #5a5a5a;
    --paper: #ffffff;
  }
  * { box-sizing: border-box; margin: 0; padding: 0; }
  html, body { width: 1200px; height: 900px; overflow: hidden; background: var(--paper); }
  body { position: relative; font-family: "Open Sans", Arial, sans-serif; }

  .display { font-family: "Graduate", "Arial Black", sans-serif; color: var(--blue); text-transform: uppercase; line-height: 1; }

  .brand-tile { position: absolute; left: 17px; top: 8px; width: 140px; height: 140px; background: linear-gradient(135deg, var(--blue) 0%, var(--blue) 50%, var(--blue-deep) 100%); }

  .slide { position: absolute; overflow: hidden; background: radial-gradient(ellipse at 50% 40%, var(--slide-mid) 0%, #151515 55%, var(--ink) 100%); }
  .slide--title { left: 98px; top: 176px; width: 562px; height: 315px; }
  .slide--thanks { left: 98px; top: 516px; width: 562px; height: 315px; }
  .slide--image { left: 704px; top: 14px; width: 462px; height: 260px; }
  .slide--bullets { left: 704px; top: 294px; width: 462px; height: 259px; }
  .slide--graphic { left: 704px; top: 571px; width: 462px; height: 259px; }

  .corner { position: absolute; width: 48px; height: 48px; background: var(--blue); }
  .corner--top { top: 0; right: 0; clip-path: polygon(0 0, 100% 0, 100% 100%); }
  .corner--bottom { bottom: 0; right: 0; width: 60px; height: 60px; clip-path: polygon(100% 0, 100% 100%, 0 100%); }
  .corner__num { position: absolute; color: var(--white); font-family: "Graduate", sans-serif; }
  .corner--top .corner__num { top: 5px; right: 6px; font-size: 10px; }
  .corner--bottom .corner__num { bottom: 6px; right: 7px; font-size: 20px; }

  .title-page__heading { position: absolute; top: 26px; width: 100%; text-align: center; font-size: 54px; }
  .title-page__reflection { position: absolute; top: 120px; width: 100%; text-align: center; font-size: 54px; transform: scaleY(-0.5); color: #444; opacity: .35; }
  .title-page__sub { position: absolute; top: 81px; width: 100%; text-align: center; color: var(--white); font-size: 12px; letter-spacing: .2px; }
  .title-page__badge { position: absolute; left: 232px; top: 152px; width: 118px; height: 118px; border: 5px solid var(--blue); border-radius: 50%; background: #0d1b22; display: flex; align-items: center; justify-content: center; }
  .title-page__url { position: absolute; top: 286px; width: 100%; text-align: center; color: #4a4a4a; font-size: 12px; }

  .brand-name { color: var(--white); font-weight: 700; font-size: 13px; }

  .thanks__heading { position: absolute; top: 128px; left: 136px; font-size: 56px; }
  .thanks__reflection { position: absolute; top: 168px; left: 136px; font-size: 56px; transform: scaleY(-0.45); color: var(--blue); opacity: .15; }

  .band { position: absolute; left: 0; right: 0; bottom: 0; height: 62px; background: linear-gradient(90deg, #0c1a24 0%, var(--blue-band) 50%, #07121a 100%); }
  .band__title { position: absolute; left: 15px; top: 6px; font-size: 28px; padding-bottom: 2px; border-bottom: 2px solid var(--blue); }
  .band__sub { position: absolute; left: 38px; top: 40px; color: #cfd6db; font-size: 7.5px; }
  .band__brand { position: absolute; right: 10px; top: 32px; display: flex; align-items: center; gap: 5px; }
  .band__dot { width: 12px; height: 12px; border: 2px solid var(--blue); border-radius: 50%; }

  .image-frame { position: absolute; left: 12px; top: 14px; width: 164px; height: 168px; background: #2b2b2b; }
  .image-frame__fill { position: absolute; left: 4px; top: 5px; width: 160px; height: 158px; background: linear-gradient(135deg, var(--blue) 0%, var(--blue) 55%, var(--blue-deep) 100%); }
  .image-frame__label { position: absolute; left: 184px; top: 46px; writing-mode: vertical-rl; transform: rotate(180deg); color: var(--white); font-size: 9px; }

  .rule { position: absolute; left: 12px; top: 14px; width: 410px; height: 1px; background: #555; }
  .rule__node { position: absolute; left: 8px; top: 10px; width: 10px; height: 10px; border: 2px solid var(--blue); border-radius: 50%; background: #111; }

  .bullets { position: absolute; left: 44px; top: 38px; list-style: none; }
  .bullets__main { display: flex; align-items: center; gap: 8px; font-size: 16px; }
  .bullets__main::before { content: ""; width: 12px; height: 12px; border: 3px solid var(--blue); border-radius: 50%; }
  .bullets__sub { list-style: none; margin: 6px 0 0 36px; }
  .bullets__sub li { display: flex; align-items: center; gap: 6px; color: #c8c8c8; font-size: 9px; text-transform: uppercase; height: 23px; }
  .bullets__sub li::before { content: ""; width: 9px; height: 9px; border: 2px solid #555; border-radius: 50%; }

  .chart { position: absolute; left: 0; top: 0; }
</style>
</head>
<body>
  <div class="brand-tile" role="img" aria-label="Blue square tile with a white ticket-shaped sample image"></div>

  <section class="slide slide--title">
    <h1 class="display title-page__heading">Title Page</h1>
    <div class="display title-page__reflection" aria-hidden="true">Title Page</div>
    <p class="title-page__sub">DETAILS OF PRESENTATION / NAME OF PRESENTOR</p>
    <div class="title-page__badge"><span class="brand-name">Kelvanta</span></div>
    <p class="title-page__url">http://www.yoursite.net/</p>
    <div class="corner corner--bottom"><span class="corner__num">01</span></div>
  </section>

  <section class="slide slide--thanks">
    <h2 class="display thanks__heading">Thank You</h2>
    <div class="display thanks__reflection" aria-hidden="true">Thank You</div>
    <div class="corner corner--bottom"><span class="corner__num">X</span></div>
  </section>

  <section class="slide slide--image">
    <div class="image-frame"><div class="image-frame__fill" role="img" aria-label="Sample image area"></div></div>
    <span class="image-frame__label">sample image placement</span>
    <div class="corner corner--top"><span class="corner__num">02</span></div>
    <div class="band">
      <h2 class="display band__title">Slide Title</h2>
      <p class="band__sub">DETAILS OF SLIDE / NAME OF PRESENTOR</p>
      <div class="band__brand"><span class="brand-name">Kelvanta</span><span class="band__dot"></span></div>
    </div>
  </section>

  <section class="slide slide--bullets">
    <div class="rule"></div><div class="rule__node"></div>
    <ul class="bullets">
      <li class="display bullets__main">Main Bullet</li>
      <li>
        <ul class="bullets__sub">
          <li>Sub bullet form</li>
          <li>Sub bullet form</li>
          <li>Sub bullet form</li>
        </ul>
      </li>
    </ul>
    <div class="corner corner--top"><span class="corner__num">03</span></div>
    <div class="band">
      <h2 class="display band__title">Slide Title</h2>
      <p class="band__sub" style="left:135px">BULLET FORM</p>
      <div class="band__brand"><span class="brand-name">Kelvanta</span><span class="band__dot"></span></div>
    </div>
  </section>

  <section class="slide slide--graphic">
    <div class="rule"></div><div class="rule__node"></div>
    <svg class="chart" width="462" height="200" viewBox="0 0 462 200" aria-label="Pyramid and pie chart">
      <polygon points="114,76 139,76 152,105 101,105" fill="#7dc242"/>
      <polygon points="80,107 174,107 184,137 69,137" fill="#29a8e0"/>
      <polygon points="69,139 184,139 184,143 69,143" fill="#1a6fa8"/>
      <polygon points="52,141 202,141 216,170 33,170" fill="#5b5b5b"/>
      <polygon points="33,170 216,170 216,176 33,176" fill="#333"/>
      <g transform="translate(333,116)" stroke="#111" stroke-width="1.5">
        <ellipse cx="0" cy="12" rx="67" ry="65" fill="#2a2a2a"/>
        <path d="M0,0 L0,-67 A67,67 0 0,1 35,-57 Z" fill="#2fb56f"/>
        <path d="M0,0 L35,-57 A67,67 0 0,1 62,-25 Z" fill="#13a08e"/>
        <path d="M0,0 L62,-25 A67,67 0 0,1 58,34 Z" fill="#29a8e0"/>
        <path d="M0,0 L58,34 A67,67 0 0,1 -12,66 Z" fill="#c4996a"/>
        <path d="M0,0 L-12,66 A67,67 0 0,1 -66,8 Z" fill="#6a6a6a"/>
        <path d="M0,0 L-66,8 A67,67 0 0,1 -46,-49 Z" fill="#8cc63f"/>
        <path d="M0,0 L-46,-49 A67,67 0 0,1 0,-67 Z" fill="#119948"/>
      </g>
    </svg>
    <div class="corner corner--top"><span class="corner__num">04</span></div>
    <div class="band">
      <h2 class="display band__title">Graphic Slide</h2>
      <p class="band__sub">DETAILS OF SLIDE / NAME OF PRESENTOR</p>
      <div class="band__brand"><span class="brand-name">Kelvanta</span><span class="band__dot"></span></div>
    </div>
  </section>
</body>
</html>
```